wig manufacturer
I would like something very upscale.highend looking
maybe mat chrome card with shiney chrome
or something like the Quince business card very clean and simple white with the logo in silver
Target Market(s)
upscale women
Industry/Entity Type
Business
Contact Information for Business Card
OUR LOGO
company name:Rosamund Wigs
48E92Avenue Harold Pinsett
New York,N.Y 10018
Tel:212-5550148
1800-5550193
email:tressline@mailbox.example
website:Rosamundwigs.example

```html
<!DOCTYPE html>
<html lang="en">
<head>
<meta charset="utf-8">
<title>Rosamund Wigs — Business Card</title>
<link rel="stylesheet" href="https://fonts.googleapis.com/css2?family=Gelasio:wght@400&display=swap">
<style>
  :root {
    --backdrop: #d9d9d9;
    --card: #ffffff;
    --brand-navy: #2c4586;
    --ink: #5a5a5a;
    --ink-strong: #4a4a4a;
  }
  html, body {
    margin: 0;
    width: 1200px;
    height: 900px;
    overflow: hidden;
    background: var(--backdrop);
  }
  .stage {
    width: 1200px;
    height: 900px;
    display: flex;
    align-items: center;
    justify-content: center;
  }
  .business-card {
    position: relative;
    width: 840px;
    height: 480px;
    background: var(--card);
    border-radius: 22px;
    box-shadow: 0 10px 30px rgba(0,0,0,0.18);
    font-family: "Gelasio", Georgia, serif;
    text-align: center;
    color: var(--ink);
  }
  .brand-mark {
    position: absolute;
    top: 44px;
    left: 0;
    right: 0;
    display: flex;
    flex-direction: column;
    align-items: center;
    gap: 10px;
  }
  .brand-name {
    font-size: 22px;
    color: var(--brand-navy);
    line-height: 1;
  }
  .brand-square {
    width: 96px;
    height: 96px;
    background: var(--brand-navy);
  }
  .company-name {
    position: absolute;
    top: 232px;
    left: 0;
    right: 0;
    margin: 0;
    font-size: 38px;
    font-weight: 400;
    letter-spacing: 2px;
    color: var(--ink-strong);
  }
  .contact-lines {
    position: absolute;
    top: 300px;
    left: 0;
    right: 0;
    margin: 0;
    font-size: 19px;
    line-height: 27px;
    font-style: normal;
  }
</style>
</head>
<body>
<main class="stage">
  <section class="business-card">
    <div class="brand-mark">
      <span class="brand-name">rosamund</span>
      <span class="brand-square"></span>
    </div>
    <h1 class="company-name">ROSAMUND WIGS</h1>
    <address class="contact-lines">
      Tel: 212-5550148 1800-5550193<br>
      email: tressline@mailbox.example web: Rosamundwigs.example<br>
      48E92Avenue Harold Pinsett New York,N.Y 10018
    </address>
  </section>
</main>
</body>
</html>
```